LumaCREST new era @ Hyper Digitalization

We need a Brochure that show all our product, services and consulting related to Hyper Digitalization into the industrial internet of things world.
We need a document that can be handled as a electronic brochure, this means that we need to show strong corporate presence, with strong skill of technology, and we have credentials and key sucess projects related to Manufacturing industries.
Key industries that we attend: Automotive, Chemical, Food and Beverage, Mining, Paper and Pulp, Oil and Gas, Energy Management.
We save money to our customer in 6 ways: 1) Eficiency in operation 2) Production Control 3) Hyper Digitalization of Thing Optimizing asset ussage 4) Maintenance and predictive of assets risks 5) Quality Control reducing Cost 6) Augmented Reality in operation and control
Target Market(s)
Manufacturing Industry. CEO of companies that has challenges of saving operation costs into plants of manufacturing.
Industry/Entity Type
Software
Other font styles liked:
- MONTSERRAT
Requirements
Must have
- Technology Enviroment, our logo, our expertise, simple message about what our company does and the DNA, infography of the company, cases of sucess, cases of savings $ using our tecnology and services, what we can do for the customer in a few words
Nice to have
- standarize our colors related to our presentation, futuristic, information related to Artificial Inteligence related to machinery
Should not have
- old version of technology,

```html
<!DOCTYPE html>
<html lang="es">
<head>
<meta charset="utf-8">
<title>LumaCREST 2021 – Hyper Digitalization</title>
<link rel="stylesheet" href="https://fonts.googleapis.com/css2?family=Montserrat:wght@300;400;500;600;700;800&display=swap">
<style>
  :root{
    --navy:#0e3b5e;
    --blue:#0a7bc2;
    --grey:#8b9096;
    --ink:#2b2f33;
    --board:#e7e7e7;
    --white:#ffffff;
  }
  *{box-sizing:border-box;margin:0;padding:0}
  html,body{width:1200px;height:3000px;overflow:hidden}
  body{background:var(--board);font-family:"Montserrat",Arial,sans-serif;color:var(--ink);position:relative}
  .page{position:absolute;left:287px;width:627px;height:444px;background:var(--white);overflow:hidden;box-shadow:0 2px 6px rgba(0,0,0,.18)}
  .abs{position:absolute}
  .brand{font-family:"Montserrat",Arial,sans-serif;font-weight:600;color:var(--blue);letter-spacing:.5px;white-space:nowrap}
  .body-text{font-size:8.6px;line-height:10.6px;font-weight:400;text-align:justify}
  .body-text p{margin-bottom:10.6px}
  .body-text p:last-child{margin-bottom:0}
  .body-text strong,.quote-box strong{font-weight:700}
  .photo{position:absolute}
  .framed{border:3px solid var(--white);box-shadow:0 1px 5px rgba(0,0,0,.35)}

  /* footer */
  .page-footer .brand{position:absolute;left:31px;top:381px;font-size:21px}
  .footer-rule{position:absolute;left:192px;top:388px;width:390px;height:1px;background:#c9ced3}
  .footer-tab{position:absolute;left:403px;top:388px;width:175px;height:26px}
  .footer-url{position:absolute;left:420px;top:393px;font-size:13px;font-weight:300;color:var(--white)}
  .page-num{position:absolute;left:575px;top:388px;width:24px;height:24px;border-radius:50%;background:var(--white);border:1.5px solid var(--navy);font-size:12px;font-weight:500;color:var(--navy);text-align:center;line-height:21px}

  /* cover */
  .cover-haze{left:0;top:0;width:360px;height:222px;background:linear-gradient(180deg,#d9dbde 0%,#eef0f1 55%,#fafafa 100%)}
  .cover .brand{left:30px;top:92px;font-size:38px}
  .cover-band{left:0;top:222px;width:400px;height:162px;background:var(--navy)}
  .cover-title{left:30px;top:241px;font-size:33px;font-weight:700;color:var(--white);letter-spacing:.5px}
  .cover-year{left:30px;top:280px;font-size:33px;font-weight:300;color:var(--white)}
  .cover-rule{left:30px;top:323px;width:226px;height:1px;background:#6d8aa3}
  .cover-rule-accent{left:46px;top:321px;width:40px;height:5px;border-radius:3px;background:var(--blue)}
  .cover-tag{left:30px;top:347px;font-size:17px;font-weight:700;color:var(--white);letter-spacing:.3px}
  .cover-tag span{font-weight:400;color:var(--blue)}
  .cover-url{left:31px;top:398px;font-size:15px;font-weight:400;color:var(--ink)}
  .cover-art{left:0;top:0;width:627px;height:444px}

  /* section heads */
  .section-tab{left:0;top:56px;width:19px;height:44px;background:var(--navy)}
  .section-title{left:31px;top:50px;font-size:28px;font-weight:800;color:var(--blue);letter-spacing:.2px}
  .section-sub{left:31px;top:82px;font-size:20px;font-weight:400;color:var(--ink)}

  .quote-box{background:var(--blue);color:var(--white);padding:30px 26px 20px 25px;font-size:8.6px;line-height:10.6px;font-weight:400}
  .quote-box p{margin-bottom:10.6px}
  .quote-box p:last-child{margin-bottom:0}

  .grey-title{left:33px;top:85px;font-size:17px;font-weight:700;color:var(--grey);letter-spacing:.4px}
  .side-bar{left:566px;top:90px;width:61px;height:268px;background:var(--blue)}

  /* back */
  .back .brand{left:0;width:627px;text-align:center;top:268px;font-size:29px}
  .contact{left:0;width:627px;text-align:center;font-size:15px;font-weight:300;color:var(--white)}
  .contact svg{vertical-align:-1px;margin-right:4px}
</style>
</head>
<body>

<!-- Cover -->
<section class="page cover" style="top:59px">
  <div class="abs cover-haze" role="img" aria-label="Faint grey cityscape of office towers"></div>
  <div class="abs brand">LumaCREST</div>
  <div class="abs cover-band"></div>
  <div class="abs cover-title">LUMACREST</div>
  <div class="abs cover-year">2021</div>
  <div class="abs cover-rule"></div>
  <div class="abs cover-rule-accent"></div>
  <div class="abs cover-tag">HYPER <span>DIGITALIZATION</span></div>
  <div class="abs cover-url">www.lumacrest.com</div>
  <svg class="abs cover-art" viewBox="0 0 627 444">
    <defs>
      <linearGradient id="rigSky" x1="0" y1="0" x2="0" y2="1">
        <stop offset="0" stop-color="#4b5fb0"/>
        <stop offset=".35" stop-color="#b07bb5"/>
        <stop offset=".55" stop-color="#d98a5a"/>
        <stop offset=".75" stop-color="#3a3d55"/>
        <stop offset="1" stop-color="#1f2d45"/>
      </linearGradient>
      <clipPath id="coverClip"><rect width="627" height="444"/></clipPath>
    </defs>
    <g clip-path="url(#coverClip)">
      <circle cx="648" cy="222" r="342" fill="var(--blue)"/>
      <circle cx="660" cy="222" r="328" fill="var(--white)"/>
      <circle cx="664" cy="222" r="322" fill="url(#rigSky)" role="img" aria-label="Offshore oil platform lit at dusk over the sea"/>
    </g>
  </svg>
</section>

<!-- Page 2: who we are -->
<section class="page" style="top:548px">
  <div class="abs section-tab"></div>
  <div class="abs section-title">HIPERDIGITALIZACIÓN</div>
  <div class="abs section-sub">la nueva era de la industria</div>
  <div class="abs body-text" style="left:31px;top:139px;width:306px">
    <p>LumaCrest es una empresa de software que lleva la hiperdigitalización al mundo del internet industrial de las cosas: conectamos máquinas, personas y datos en una sola plataforma para que cada planta produzca más con lo que ya tiene.</p>
    <p>Nuestro ADN: tecnología, ingeniería y resultados medibles. Ofrecemos productos, servicios y consultoría, desde el sensor en la línea hasta el motor de inteligencia artificial.</p>
    <p>La inteligencia artificial aplicada a la maquinaria aprende del comportamiento de cada activo y anticipa fallas antes de que detengan la producción.</p>
    <p>Atendemos a directores que buscan reducir los costos de operación en sus plantas de manufactura, con proyectos que se pagan en meses.</p>
    <p>Industrias clave: Automotriz, Química, Alimentos y Bebidas, Minería, Papel y Celulosa, Petróleo y Gas, y Gestión de Energía. En cada una, un mismo objetivo: operar mejor, con menos costo.</p>
  </div>
  <div class="photo framed" style="left:371px;top:141px;width:220px;height:198px;background:linear-gradient(135deg,#9fb6c6 0%,#d7e2e8 45%,#4aa3a6 70%,#c9d3d8 100%)" role="img" aria-label="Lab technician in protective suit working at stainless steel process tanks"></div>
  <div class="page-footer">
    <div class="brand">LumaCREST</div>
    <div class="footer-rule"></div>
    <svg class="footer-tab" viewBox="0 0 175 26"><polygon points="16,0 175,0 175,26 0,26" fill="var(--navy)"/></svg>
    <div class="footer-url">www.lumacrest.com</div>
    <div class="page-num">2</div>
  </div>
</section>

<!-- Page 3: six ways of saving -->
<section class="page" style="top:1040px">
  <div class="photo framed" style="left:-3px;top:52px;width:386px;height:294px;background:linear-gradient(180deg,#cfd8dc 0%,#e6e3d6 45%,#8d8a72 70%,#5a5746 100%)" role="img" aria-label="Two engineers in hard hats looking at a refinery"></div>
  <div class="abs quote-box" style="left:351px;top:87px;width:239px;height:228px">
    <p>Ahorramos dinero a nuestros clientes de seis maneras:</p>
    <p>1) Eficiencia en la operación.<br>2) Control de la producción.<br>3) Hiperdigitalización de las cosas, optimizando el uso de activos.<br>4) Mantenimiento y predicción de riesgos de los activos.<br>5) Control de calidad que reduce costos.<br>6) Realidad aumentada en operación y control.</p>
    <p>Lo que hacemos por usted, en pocas palabras: conectamos su planta, convertimos sus datos en decisiones y reducimos su costo de operación.</p>
  </div>
  <div class="page-footer">
    <div class="brand">LumaCREST</div>
    <div class="footer-rule"></div>
    <svg class="footer-tab" viewBox="0 0 175 26"><polygon points="16,0 175,0 175,26 0,26" fill="var(--navy)"/></svg>
    <div class="footer-url">www.lumacrest.com</div>
    <div class="page-num">3</div>
  </div>
</section>

<!-- Page 4: company in figures -->
<section class="page" style="top:1527px">
  <div class="abs grey-title">LUMACREST EN CIFRAS</div>
  <div class="abs body-text" style="left:33px;top:122px;width:274px">
    <p><strong>15 años</strong> de experiencia en software industrial. <strong>7 industrias</strong> atendidas. <strong>+120 plantas</strong> conectadas y <strong>+40,000 activos</strong> monitoreados en tiempo real con nuestra plataforma de internet industrial de las cosas.</p>
    <p><strong>Petróleo y Gas, y Energía:</strong> monitoreo remoto de equipos críticos y gestión del consumo energético de cada línea.</p>
    <p><strong>Automotriz, Química, Alimentos y Bebidas:</strong> control de la producción, trazabilidad y control de calidad en línea, con realidad aumentada para los operarios.</p>
    <p><strong>Minería, Papel y Celulosa:</strong> mantenimiento predictivo con inteligencia artificial que aprende de la vibración, la temperatura y la carga de cada máquina para anticipar fallas.</p>
  </div>
  <div class="abs side-bar"></div>
  <div class="photo framed" style="left:343px;top:119px;width:248px;height:98px;background:linear-gradient(180deg,#6f9fd0 0%,#a9c6e2 45%,#d98a3d 70%,#2c3b55 100%)" role="img" aria-label="Container port with cranes at dusk"></div>
  <div class="photo framed" style="left:343px;top:239px;width:248px;height:96px;background:linear-gradient(180deg,#5b6e9a 0%,#c88a8a 40%,#f0a040 70%,#6a3a2a 100%)" role="img" aria-label="Electricity pylons against a sunset sky"></div>
  <div class="page-footer">
    <div class="brand">LumaCREST</div>
    <div class="footer-rule"></div>
    <svg class="footer-tab" viewBox="0 0 175 26"><polygon points="16,0 175,0 175,26 0,26" fill="var(--navy)"/></svg>
    <div class="footer-url">www.lumacrest.com</div>
    <div class="page-num">4</div>
  </div>
</section>

<!-- Page 5: success cases -->
<section class="page" style="top:2010px">
  <div class="photo" style="left:31px;top:22px;width:562px;height:130px;background:linear-gradient(180deg,#3f6fa8 0%,#a8c3dd 40%,#d8cbb0 65%,#8a7a62 100%)" role="img" aria-label="Open-pit quarry with concrete plant and gravel piles"></div>
  <div class="abs quote-box" style="left:31px;top:154px;width:297px;height:211px;padding:14px 20px 10px 17px">
    <p><strong>Casos de éxito</strong></p>
    <p><strong>Minería:</strong> mantenimiento predictivo con inteligencia artificial en trituradoras y bandas. Paros no programados −35% y ahorro anual de US$1.2 millones.</p>
    <p><strong>Alimentos y Bebidas:</strong> control de calidad en línea y trazabilidad de lotes. Merma −22% y ahorro de US$480,000 en el primer año.</p>
    <p><strong>Automotriz:</strong> control de la producción y realidad aumentada para operarios. Eficiencia global del equipo +18% y retorno de la inversión en 9 meses.</p>
  </div>
  <div class="abs body-text" style="left:348px;top:167px;width:245px">
    <p><strong>Química:</strong> hiperdigitalización de reactores y bombas, optimizando el uso de activos. Capacidad +12% sin nueva inversión en equipo.</p>
    <p><strong>Gestión de Energía:</strong> consumo eléctrico −15% en tres plantas, con un ahorro de US$650,000 al año.</p>
    <p>“Nuestros clientes ya tenían máquinas conectadas; hoy las explotan tres o seis veces más. La hiperdigitalización es la clave para cambiar el panorama de ‘no se puede’ por una nueva forma de trabajar”, afirmó Tomás Beltrán, director general de LumaCrest.</p>
    <p>Conectamos su planta, convertimos sus datos en decisiones y reducimos su costo de operación.</p>
  </div>
  <div class="page-footer">
    <div class="brand">LumaCREST</div>
    <div class="footer-rule"></div>
    <svg class="footer-tab" viewBox="0 0 175 26"><polygon points="16,0 175,0 175,26 0,26" fill="var(--navy)"/></svg>
    <div class="footer-url">www.lumacrest.com</div>
    <div class="page-num">5</div>
  </div>
</section>

<!-- Back cover -->
<section class="page back" style="top:2495px">
  <div class="abs" style="left:230px;top:0;width:397px;height:325px;background:radial-gradient(ellipse at 80% 40%,#eceef0 0%,#f6f7f8 50%,#ffffff 100%)" role="img" aria-label="Faint technology network of connected dots"></div>
  <div class="abs brand">LumaCREST</div>
  <svg class="abs" style="left:0;top:325px" width="627" height="119" viewBox="0 0 627 119">
    <rect width="627" height="119" fill="var(--navy)"/>
    <polygon points="0,0 80,119 0,119" fill="var(--blue)"/>
    <line x1="0" y1="2" x2="79" y2="119" stroke="var(--white)" stroke-width="4"/>
  </svg>
  <div class="abs contact" style="top:340px">
    <svg width="11" height="11" viewBox="0 0 24 24"><path d="M6.6 10.8a15.2 15.2 0 006.6 6.6l2.2-2.2a1 1 0 011-.25 11.4 11.4 0 003.6.57 1 1 0 011 1V20a1 1 0 01-1 1A17 17 0 013 4a1 1 0 011-1h3.5a1 1 0 011 1c0 1.250.2 2.450.57 3.57a1 1 0 01-.25 1z" fill="var(--blue)"/></svg>555.014.2290
  </div>
  <div class="abs contact" style="top:364px">
    <svg width="11" height="9" viewBox="0 0 24 18"><rect x="1" y="1" width="22" height="16" rx="2" fill="none" stroke="var(--blue)" stroke-width="2.5"/><path d="M2 2l10 8 10-8" fill="none" stroke="var(--blue)" stroke-width="2.5"/></svg>hello@lumacrest.com
  </div>
  <div class="abs contact" style="top:388px">
    <svg width="11" height="11" viewBox="0 0 24 24"><circle cx="12" cy="12" r="10" fill="none" stroke="var(--blue)" stroke-width="2.5"/><ellipse cx="12" cy="12" rx="4.5" ry="10" fill="none" stroke="var(--blue)" stroke-width="2"/><line x1="2" y1="12" x2="22" y2="12" stroke="var(--blue)" stroke-width="2"/></svg>www.lumacrest.com
  </div>
</section>

</body>
</html>
```